Ridgeline Provisions Co Website Creation

We need a website designed that goes along with our western/cattle brand vibe that our logo has. We are going to need a couple different pages including: About Us, Meat Boxes, Recipes, Contact Us.

We are going to need a shop so that people may visit the website and order meat boxes to be shipped or delivered at their home. Our mission is to provide the highest quality meat that every family can afford.

Would love to see the website design with lots of mountain range backgrounds and create a feel of open range beef that has a tradition of providing great beef. Family owned business that has been raising cattle for over 30 years.

Love the colors of using dark greens, browns, Tans, Blacks

```html
<!DOCTYPE html>
<html lang="en">
<head>
<meta charset="utf-8">
<title>Ridgeline Provisions Co</title>
<link href="https://fonts.googleapis.com/css2?family=Anton&family=Poppins:wght@400;500;600;700&display=swap" rel="stylesheet">
<style>
:root{
  --brown:#6b4423;
  --brown-dark:#3b1f0e;
  --ink:#1c1410;
  --text:#3a3330;
  --green:#2e6b1a;
  --tan:#d8b895;
  --cream:#f6efe8;
  --grey-band:#f2f0ed;
  --panel:#f3f2f0;
  --white:#ffffff;
  --star:#f2a22c;
}
*{box-sizing:border-box;margin:0;padding:0}
html,body{width:1200px;height:3563px;overflow:hidden}
body{font-family:"Poppins",sans-serif;color:var(--text);background:var(--white);position:relative}
.abs{position:absolute}
.display{font-family:"Anton",sans-serif;color:var(--ink);text-transform:uppercase;letter-spacing:.3px;font-weight:400}
.btn{position:absolute;display:flex;align-items:center;justify-content:center;background:var(--brown);color:var(--white);border-radius:30px;font-size:13px;font-weight:500;white-space:nowrap}
.photo{position:absolute}

/* header */
.site-header{position:absolute;top:0;left:0;width:1200px;height:84px;background:var(--white)}
.brand{left:131px;top:16px;width:180px;text-align:center;font-family:"Anton",sans-serif;font-size:20px;line-height:25px;color:var(--brown-dark);white-space:nowrap}
.nav{left:502px;top:33px;font-size:13px;font-weight:500;color:var(--ink)}
.nav span{position:absolute;white-space:nowrap}
.nav .active{color:var(--brown)}

/* hero */
.hero{position:absolute;top:84px;left:0;width:1200px;height:487px;
  background:
    radial-gradient(ellipse 420px 260px at 820px 150px,rgba(235,225,200,.55),rgba(235,225,200,0) 70%),
    linear-gradient(180deg,#3f4c5a 0%,#6d7680 18%,#9a968a 34%,#7d7462 48%,#6b6a3c 62%,#5e5a24 74%,#4a4418 86%,#2f2a12 100%)}
.hero-title{left:141px;top:166px;font-size:42px;line-height:50px;color:var(--white);white-space:nowrap}
.hero-sub{left:141px;top:289px;font-size:16px;color:var(--white)}
.hero .btn{left:141px;top:344px;width:166px;height:41px;background:var(--tan);font-size:12px}

/* about */
.about-panel{left:239px;top:771px;width:714px;height:324px;background:var(--panel)}
.about-title{left:430px;top:708px;font-size:32px;white-space:nowrap}
.about-sub{left:423px;top:797px;font-size:18px;font-weight:500;color:var(--green)}
.about-text{left:423px;top:838px;width:362px;font-size:12.5px;line-height:22.5px}

/* products */
.section-title{font-size:32px;text-align:center;width:1200px;left:0}
.card{position:absolute;top:1266px;width:289px;height:263px;background:var(--white);box-shadow:0 2px 12px rgba(0,0,0,.08)}
.card .photo{left:7px;top:7px;width:275px;height:206px}
.card .name{position:absolute;left:14px;top:224px;font-family:"Anton",sans-serif;font-size:18px;color:var(--ink)}
.card .price{position:absolute;right:14px;top:227px;font-size:14px;font-weight:600;color:var(--brown)}

/* recipes */
.recipes{position:absolute;top:1698px;left:0;width:1200px;height:497px;background:var(--cream)}
.recipe{position:absolute;top:130px;width:213px;height:247px}
.recipe span{position:absolute;bottom:12px;width:100%;text-align:center;color:var(--white);font-size:14px;font-weight:500}
.round{position:absolute;width:36px;height:36px;border-radius:50%;display:flex;align-items:center;justify-content:center}

/* testimonials */
.quote-text{left:141px;top:2474px;width:480px;text-align:center;font-size:13px;line-height:23px}
.avatar{position:absolute;border-radius:50%}

/* newsletter */
.newsletter{position:absolute;top:2823px;left:0;width:1200px;height:337px;background:var(--grey-band)}
.news-title{top:80px;left:0;width:1200px;text-align:center;font-size:32px;line-height:46px}
.news-text{top:171px;left:0;width:1200px;text-align:center;font-size:12.5px;line-height:21px}
.subscribe{left:343px;top:225px;width:514px;height:56px;background:var(--white);border-radius:30px;box-shadow:0 2px 10px rgba(0,0,0,.06)}

/* footer */
.footer{position:absolute;top:3160px;left:0;width:1200px;height:403px;background:var(--brown);color:var(--white)}
.foot-brand{left:121px;top:138px;width:220px;text-align:center;font-family:"Anton",sans-serif;font-size:30px;line-height:40px;white-space:nowrap}
.foot-head{font-family:"Anton",sans-serif;font-size:17px;top:76px;letter-spacing:.3px;font-weight:400}
.foot-links{font-size:13px;line-height:29px;top:113px}
.contact-item{position:absolute;left:852px;font-size:13px;display:flex;gap:10px;align-items:flex-start;line-height:18px}
.divider{left:141px;top:342px;width:918px;height:1px;background:rgba(255,255,255,.35)}
.social{position:absolute;top:3519px;width:25px;height:25px;border-radius:50%;background:var(--white)}
</style>
</head>
<body>

<header class="site-header">
  <div class="abs brand">RIDGELINE<br>PROVISIONS CO</div>
  <nav class="abs nav">
    <span class="active" style="left:0">Home</span>
    <span style="left:70px">About Us</span>
    <span style="left:160px">Meat Boxes</span>
    <span style="left:265px">Recipes</span>
    <span style="left:347px">Contact Us</span>
  </nav>
  <div class="btn" style="left:952px;top:22px;width:107px;height:42px">Shop Now</div>
</header>

<section class="hero" role="img" aria-label="Mountain range above a forest valley and lake at sunrise">
  <h1 class="abs display hero-title">Top quality meat,<br>affordable for every family</h1>
  <p class="abs hero-sub">Premium, Family-Raised Beef – Delivered to Your Door.</p>
  <div class="btn">Explore Meat Boxes</div>
</section>

<section class="about">
  <div class="abs about-panel"></div>
  <div class="photo" role="img" aria-label="Cattle grazing in a green pasture below a mountain" style="left:141px;top:657px;width:246px;height:315px;background:linear-gradient(180deg,#6f7e8c 0%,#a9b3b8 30%,#c3c7c4 46%,#7d8f5a 56%,#78a044 70%,#5f8a33 85%,#4a6b28 100%)"></div>
  <div class="photo" role="img" aria-label="Ranch family walking through a field by a barn" style="left:817px;top:698px;width:242px;height:242px;background:linear-gradient(180deg,#a8aaa2 0%,#7a6a58 25%,#5a4432 45%,#6a7a3c 65%,#4d6a2a 82%,#3a4e20 100%)"></div>
  <h2 class="abs display about-title">About Ridgeline</h2>
  <h3 class="abs about-sub">30 years of raising cattle</h3>
  <p class="abs about-text">There are many variations of passages of Lorem Ipsum available, but the majority have suffered alteration in some form, by injected humour, or randomised words which don't look even slightly believable. If you are going to use a passage of Lorem Ipsum, you need to be sure there isn't anything embarrassing hidden in the middle of text.</p>
  <div class="btn" style="left:423px;top:1017px;width:113px;height:42px">Learn More</div>
</section>

<section class="products">
  <h2 class="abs display section-title" style="top:1188px">Our Products</h2>
  <div class="card" style="left:141px">
    <div class="photo" role="img" aria-label="Raw ribeye steaks in a tray on wood" style="background:radial-gradient(ellipse 120px 70px at 50% 45%,#d98a92 0%,#c87a7e 50%,rgba(90,80,70,0) 100%),linear-gradient(180deg,#7a6654 0%,#5e4e40 70%,#3a322a 100%)"></div>
    <span class="name">RIBEYE</span><span class="price">$20.00</span>
  </div>
  <div class="card" style="left:456px">
    <div class="photo" role="img" aria-label="Packaged tri tip cuts in a clear box" style="background:radial-gradient(ellipse 120px 70px at 50% 50%,#c8606a 0%,#d8909a 55%,rgba(240,240,240,0) 100%),linear-gradient(180deg,#f2f2f2,#e2e2e2)"></div>
    <span class="name">TRI TIP</span><span class="price">$18.00</span>
  </div>
  <div class="card" style="left:770px">
    <div class="photo" role="img" aria-label="Tenderloin cut in a black tray" style="background:radial-gradient(ellipse 90px 30px at 50% 58%,#c24a56 0%,#b04450 60%,rgba(30,30,30,0) 100%),radial-gradient(ellipse 140px 45px at 50% 66%,#222 0%,#2a2a2a 70%,rgba(212,214,216,0) 100%),linear-gradient(180deg,#d6d8da,#c8cacc)"></div>
    <span class="name">TENDERLOIN</span><span class="price">$22.00</span>
  </div>
  <div class="btn" style="left:546px;top:1565px;width:106px;height:41px">Shop Now</div>
</section>

<section class="recipes">
  <h2 class="abs display" style="left:141px;top:52px;font-size:30px">Our Delicious Recipes</h2>
  <div class="btn" style="left:911px;top:54px;width:147px;height:40px">View All Recipes</div>
  <div class="recipe" role="img" aria-label="Grilled sliced steak with herbs" style="left:141px;background:radial-gradient(ellipse 90px 60px at 55% 55%,#8a3a30 0%,rgba(60,30,20,0) 100%),linear-gradient(180deg,#2a201a,#4a3024 55%,#1e140e)"><span>Natural Prime Beef</span></div>
  <div class="recipe" role="img" aria-label="Roasted lamb shank with vegetables" style="left:376px;background:radial-gradient(ellipse 90px 70px at 50% 55%,#6a4026 0%,rgba(60,40,25,0) 100%),linear-gradient(180deg,#4a3222,#3a2a1c 55%,#2f3a1a)"><span>Natural Prime Beef</span></div>
  <div class="recipe" role="img" aria-label="Braised short rib with potatoes and greens" style="left:610px;background:radial-gradient(ellipse 90px 60px at 45% 65%,#4a2e20 0%,rgba(40,30,20,0) 100%),linear-gradient(180deg,#3d6a2a,#5a4a30 45%,#2a1d15)"><span>Natural Prime Beef</span></div>
  <div class="recipe" role="img" aria-label="Barbecue beef with corn" style="left:845px;background:radial-gradient(ellipse 100px 70px at 45% 60%,#5a2a1c 0%,rgba(60,30,20,0) 100%),linear-gradient(180deg,#c8902a,#8a5224 45%,#2a1a12)"><span>Natural Prime Beef</span></div>
  <div class="round" style="left:557px;top:413px;border:1.5px solid var(--brown)">
    <svg width="12" height="12" viewBox="0 0 12 12"><path d="M8 1 3 6l5 5" fill="none" stroke="#6b4423" stroke-width="2"/></svg>
  </div>
  <div class="round" style="left:607px;top:413px;background:var(--brown)">
    <svg width="12" height="12" viewBox="0 0 12 12"><path d="M4 1l5 5-5 5" fill="none" stroke="#fff" stroke-width="2"/></svg>
  </div>
</section>

<section class="testimonials">
  <h2 class="abs display" style="left:121px;top:2294px;width:520px;text-align:center;font-size:30px;white-space:nowrap">What our client say about us</h2>
  <svg class="abs" style="left:351px;top:2368px" width="58" height="56" viewBox="0 0 58 56"><path d="M24 4C10 10 2 20 2 34c0 11 6 18 14 18 7 0 12-5 12-12s-5-11-11-11c-1 0-2 0-3 1 1-8 6-14 14-18zM54 4C40 10 32 20 32 34c0 11 6 18 14 18 7 0 12-5 12-12s-5-11-11-11c-1 0-2 0-3 1 1-8 6-14 14-18z" fill="#d7d7d7"/></svg>
  <svg class="abs" style="left:331px;top:2438px" width="98" height="18" viewBox="0 0 98 18">
    <g fill="#f2a22c">
      <path id="st" d="M9 1l2.4 5 5.4.7-4 3.8 1 5.4L9 13.3 4.2 15.9l1-5.4-4-3.8 5.4-.7z"/>
      <use href="#st" x="20"/><use href="#st" x="40"/><use href="#st" x="60"/><use href="#st" x="80"/>
    </g>
  </svg>
  <p class="abs quote-text">There are many variations of passages of Lorem Ipsum available, but the majority have suffered alteration in some form, by injected humour, or randomised words which don't look even slightly believable. If you are going to use a passage of Lorem Ipsum.</p>
  <div class="photo" role="img" aria-label="Wooden board with assorted raw meats and herbs" style="left:17px;top:2592px;width:163px;height:97px;border-radius:8px;background:radial-gradient(ellipse 60px 35px at 50% 50%,#a8303e 0%,rgba(168,48,62,0) 100%),linear-gradient(135deg,#c7935a,#b07a48)"></div>
  <svg class="abs" style="left:240px;top:2623px" width="12" height="16" viewBox="0 0 12 16"><path d="M9 2 3 8l6 6" fill="none" stroke="#3a3330" stroke-width="2"/></svg>
  <div class="avatar" role="img" aria-label="Client portrait" style="left:270px;top:2607px;width:48px;height:48px;background:#9a9a9a"></div>
  <div class="avatar" role="img" aria-label="Client portrait" style="left:341px;top:2592px;width:78px;height:78px;background:#7a3030;border:4px solid #fff;box-shadow:0 2px 10px rgba(0,0,0,.2)"></div>
  <div class="avatar" role="img" aria-label="Client portrait" style="left:442px;top:2607px;width:48px;height:48px;background:#b0b0b0"></div>
  <svg class="abs" style="left:508px;top:2623px" width="12" height="16" viewBox="0 0 12 16"><path d="M3 2l6 6-6 6" fill="none" stroke="#3a3330" stroke-width="2"/></svg>
  <p class="abs" style="left:141px;top:2690px;width:480px;text-align:center;font-weight:700;font-size:14px;color:var(--ink)">Dale Harmon</p>
  <svg class="abs" style="left:357px;top:2721px" width="46" height="8" viewBox="0 0 46 8"><circle cx="4" cy="4" r="3" fill="#ddd"/><circle cx="17" cy="4" r="3.5" fill="#3b1f0e"/><circle cx="30" cy="4" r="3" fill="#ddd"/><circle cx="42" cy="4" r="3" fill="#ddd"/></svg>
  <div class="photo" role="img" aria-label="Grilled beef medallions on a white plate" style="left:722px;top:2288px;width:337px;height:444px;background:radial-gradient(ellipse 140px 110px at 45% 52%,#4a2a1c 0%,#6a4030 45%,rgba(232,226,218,0) 100%),radial-gradient(ellipse 260px 240px at 50% 55%,#f0ece6 0%,#e4ded6 70%,rgba(140,110,70,0) 100%),linear-gradient(160deg,#7a5a28,#3a2a1c)"></div>
</section>

<section class="newsletter">
  <h2 class="abs display news-title">Join our family of satisfied<br>customers!</h2>
  <p class="abs news-text">It is a long established fact that a reader will be distracted by the<br>readable content of a page when looking at its layout.</p>
  <div class="abs subscribe">
    <svg class="abs" style="left:20px;top:21px" width="19" height="14" viewBox="0 0 19 14"><rect width="19" height="14" rx="2" fill="#1c1410"/><path d="M1 2l8.5 6L18 2" fill="none" stroke="#fff" stroke-width="1.5"/></svg>
    <span class="abs" style="left:50px;top:18px;font-size:13px;color:#666">Enter your email address</span>
    <div class="btn" style="left:369px;top:7px;width:137px;height:42px">Subscribe Now</div>
  </div>
  <div class="photo" role="img" aria-label="Stacked seared steak pieces with herbs and peppercorns" style="left:968px;top:66px;width:180px;height:229px;background:radial-gradient(ellipse 60px 105px at 50% 50%,#4a2a20 0%,#6a3a2a 55%,rgba(242,240,237,0) 100%)"></div>
</section>

<footer class="footer">
  <div class="abs foot-brand">RIDGELINE<br>PROVISIONS CO</div>
  <h4 class="abs foot-head" style="left:502px">QUICK LINKS</h4>
  <div class="abs foot-links" style="left:502px">Home<br>About Us<br>Meat Boxes<br>Recipes<br>Shop</div>
  <h4 class="abs foot-head" style="left:672px">RESOURCES</h4>
  <div class="abs foot-links" style="left:672px">Privacy Policy<br>Terms Of Service<br>Contact Us</div>
  <h4 class="abs foot-head" style="left:852px">CONTACT INFO</h4>
  <div class="contact-item" style="top:118px">
    <svg width="16" height="18" viewBox="0 0 16 18"><path d="M8 1a5 5 0 0 0-5 5c0 4 5 9 5 9s5-5 5-9a5 5 0 0 0-5-5z" fill="none" stroke="#fff" stroke-width="1.5"/><circle cx="8" cy="6" r="1.8" fill="#fff"/></svg>
    <span>123 Lorem ipsum dummy,<br>#567 Dummy road 1234</span>
  </div>
  <div class="contact-item" style="top:172px">
    <svg width="16" height="13" viewBox="0 0 16 13"><rect width="16" height="12" rx="1.5" fill="#fff"/><path d="M1 1.5l7 5 7-5" fill="none" stroke="#6b4423" stroke-width="1.3"/></svg>
    <span>info@ridgelineprovisions.com</span>
  </div>
  <div class="contact-item" style="top:205px">
    <svg width="16" height="16" viewBox="0 0 16 16"><path d="M3 1l3 3-2 2c1 2.5 3 4.5 6 6l2-2 3 3-2 2C7 15 1 9 1 3z" fill="#fff"/></svg>
    <span>123-456-7890</span>
  </div>
  <div class="abs divider"></div>
  <p class="abs" style="left:141px;top:362px;font-size:12.5px">© 2024 Ridgeline Provisions Co. All Rights Reserved.</p>
</footer>
<div class="social" style="left:926px"></div>
<div class="social" style="left:962px"></div>
<div class="social" style="left:997px"></div>
<div class="social" style="left:1032px"></div>

</body>
</html>
```